University Alumni committee needs a new membership card design

BLRTN is the Singapore Chapter of the Marlowe University Alumni. We are embarking on a membership card project called Marlowe Bridge which aims to bring benefits and perks to our alumni members through partnership with merchants.

We need someone to do:
1) an adapted design of our logo to add the word, 'Bridge' and
2) produce both a membership card design
3) a A4 letterhead design which we intend to have our welcome message and stick on the card to mail it to our alumni members.

The final design should have sufficient space for us to print the name, membership ID and date of issue on the card and communicate the prestige of being in the BLRTN membership.

Colour guidelines already provided in attachment.

Target Market(s)

Working adults

Industry/Entity Type

University

Requirements
Must have
• 1) an adapted design of our logo to add the word, 'Bridge' and
• 2) produce both a membership card design
• 3) a A4 letterhead design which we intend to have our welcome message and stick on the card to mail it to our alumni members.

```html
<!DOCTYPE html>
<html lang="en">
<head>
<meta charset="utf-8">
<title>Marlowe Bridge Singapore Alumni — Letterhead</title>
<link href="https://fonts.googleapis.com/css2?family=Source+Sans+3:wght@400;600&display=swap" rel="stylesheet">
<style>
  :root {
    --backdrop: #a6fcfe;
    --paper: #ffffff;
    --ink-dark: #161616;
    --stripe: #8e9794;
    --gold: #a8891c;
    --white: #ffffff;
  }
  * { margin: 0; padding: 0; box-sizing: border-box; }
  html, body {
    width: 1200px; height: 1200px; overflow: hidden;
    background: var(--backdrop);
    font-family: "Source Sans 3", "Myriad Pro", sans-serif;
  }
  .canvas { position: relative; width: 1200px; height: 1200px; }
  .letterhead {
    position: absolute; left: 202px; top: 38px;
    width: 796px; height: 1124px;
    background: var(--paper);
  }
  .header-stripes {
    position: absolute; left: 18px; top: 24px;
    width: 610px; height: 63px;
  }
  .brand-block {
    position: absolute; left: 628px; top: 24px;
    width: 168px; height: 63px;
    background: var(--ink-dark);
    color: var(--white);
  }
  .brand-name {
    position: absolute; left: 8px; top: 4px;
    display: flex; align-items: center; gap: 5px;
    font-size: 31px; font-weight: 400; line-height: 1;
    letter-spacing: 0.2px;
  }
  .brand-mark {
    width: 27px; height: 27px; background: var(--gold);
  }
  .brand-sub {
    position: absolute; left: 8px; top: 36px;
    width: 129px; display: flex; align-items: center; gap: 3px;
    font-size: 7.5px; line-height: 1;
  }
  .brand-sub::before, .brand-sub::after {
    content: ""; flex: 1; height: 1px; background: var(--white);
  }
  .brand-sub::before { flex: 2.4; }
  .brand-chapter {
    position: absolute; left: 8px; top: 44px;
    font-size: 11px; letter-spacing: 2.1px; line-height: 1;
  }
  .contact-line {
    position: absolute; left: 0; right: 0; top: 1085px;
    display: flex; justify-content: center; gap: 14px;
    color: var(--gold); font-size: 13px; white-space: nowrap;
  }
</style>
</head>
<body>
<div class="canvas">
  <section class="letterhead">
    <svg class="header-stripes" viewBox="0 0 610 63" aria-hidden="true">
      <defs>
        <linearGradient id="stripe-fade" x1="0" x2="1" y1="0" y2="0">
          <stop offset="0" stop-color="#ffffff"/>
          <stop offset="0.35" stop-color="#e2e6e5"/>
          <stop offset="1" stop-color="#8e9794"/>
        </linearGradient>
      </defs>
      <g fill="url(#stripe-fade)">
        <rect x="0" y="0" width="610" height="3"/>
        <rect x="0" y="6" width="610" height="3"/>
        <rect x="0" y="12" width="610" height="3"/>
        <rect x="0" y="18" width="610" height="3"/>
        <rect x="0" y="24" width="610" height="3"/>
        <rect x="0" y="30" width="610" height="3"/>
        <rect x="0" y="36" width="610" height="3"/>
        <rect x="0" y="42" width="610" height="3"/>
        <rect x="0" y="48" width="610" height="3"/>
        <rect x="0" y="54" width="610" height="3"/>
        <rect x="0" y="60" width="610" height="3"/>
      </g>
    </svg>
    <div class="brand-block">
      <div class="brand-name">Marlowe<span class="brand-mark"></span></div>
      <div class="brand-sub">Bridge</div>
      <div class="brand-chapter">Singapore Alumni</div>
    </div>
    <footer class="contact-line">
      <span>14 Kembangan Rise, Singapore 418230</span>
      <span>T: +65 6481 2270</span>
      <span>F: +65 6481 2271</span>
      <span>E: alumni@marlowe.edu.sg</span>
    </footer>
  </section>
</div>
</body>
</html>
```